Landing Page for Marketing Campaigns

We need two pages: a Campaign Page and a Landing Page for a marketing campaign for Velora Nexa (www.veloranexa.co) WE will be running online and offline campaign that will drive traffic to this page.

The campaign page is a 480X60 or 336X280 pixels size subpage that will be embedded into other webpages. It needs to be catchy with a one line of text - which we will test different copies for A/B testing. It should also have the logo - see attached png's.

The landing page will need the following sections:

• INTRO SECTION – Some kind of image that represents us but eventually will be replaced a video.

• AN INTRO PARAGRAPH – We'd like to do some A/B testing here to test messaging.

• PRICING – some info on pricing. Pricing of product and key highlights of what you get with that pricing. Will provide content.

• SCHEDULE A DEMO – ACTION we want to drive. Take a Product tour.

• ABOUT & CONTACT US –

The landing page does not need to have the same look and feel of the website - we leave this creativity up to the designer. The only thing you need to use is our logo.

Velora Nexa Background:

Velora Nexa platform is digitizing Brick & Mortar chains by offering complete sourcing to sales integration allowing
realtime visibility and control over every aspect of its business. Chains can immediately become omnichannel increasing their reach and providing innovative customer experiences.

Velora Nexa’ platform is a pay as you go, affordable cloud-based SaaS that chains can subscribe to with no IT department, no hardware or software to maintain, 24X7 uptime, and easy to use plug and play solutions.

Target Market(s)

Chain Restaurants and Retailers -

Industry/Entity Type

Restaurant

Coding

Coded - Design and coding required

Number of Pages Required

2 page

Font styles to use
Sans Serif

Requirements
Must have
• We will use the logo from our website www.veloranexa.co and use colors that work with the logo but beyond that you do not need to adhere to the website. We're looking for a great landing page which we will drive traffic to from our marketing campaigns.
• I've requested 2 pages and the first page should be the actual landing page. The second page should be an ad that drives traffic to that page that can be used in an email marketing campaign so the two should go together.
Nice to have
• The page should be clean and inviting to restaurant and retail owners of chains. We are trying to convince them to give us a call and get a demo of our product. Eventually we want them to buy our product.
• To see more details about our product please see our website.

```html
<!DOCTYPE html>
<html lang="en">
<head>
<meta charset="utf-8">
<title>Velora Nexa — Landing Page</title>
<link href="https://fonts.googleapis.com/css2?family=Montserrat:wght@400;500;700&family=Open+Sans:ital,wght@0,400;0,600;0,700;1,400&display=swap" rel="stylesheet">
<style>
:root{
  --navy:#1c3a5e;
  --teal:#1fb79a;
  --gold:#fdb415;
  --red:#dc1a2a;
  --grey-title:#8a8a8a;
  --text:#444;
  --muted:#777;
  --line:#d9d9d9;
  --footer-bg:#f1f1f1;
  --white:#fff;
}
*{box-sizing:border-box;margin:0;padding:0}
html,body{width:709px;height:1200px;overflow:hidden;background:var(--white)}
body{position:relative;font-family:"Open Sans",sans-serif;color:var(--text)}
.abs{position:absolute}

/* header */
.site-header{left:0;top:0;width:709px;height:31px;background:var(--white);box-shadow:0 1px 3px rgba(0,0,0,.15);z-index:2}
.brand{left:96px;top:7px;display:flex;align-items:center;gap:5px;font-family:"Montserrat",sans-serif;font-weight:700;font-size:14px;color:var(--navy)}
.brand-mark{width:12px;height:12px;background:var(--navy)}
.main-nav{right:114px;top:11px;display:flex;gap:15px;font-family:"Montserrat",sans-serif;font-weight:700;font-size:7.5px;color:#555;text-transform:uppercase}
.main-nav .active{color:var(--teal)}

/* hero */
.hero{left:0;top:31px;width:709px;height:339px;background:linear-gradient(135deg,#6d8a55 0%,#9bb07c 35%,#b9a99b 55%,#4d5e3c 80%,#7a9460 100%)}
.play{left:50%;top:50%;transform:translate(-50%,-50%)}

/* welcome */
.welcome{left:0;top:370px;width:709px;height:137px;background:var(--navy);color:var(--white);text-align:center}
.welcome h1{position:absolute;top:16px;width:100%;font-family:"Montserrat",sans-serif;font-weight:700;font-size:14px}
.welcome p{position:absolute;left:146px;top:47px;width:417px;font-size:7.6px;line-height:11px}
.btn{display:inline-flex;align-items:center;justify-content:center;font-family:"Open Sans",sans-serif;font-weight:700;font-size:7px;color:var(--white);text-transform:uppercase;border-radius:4px}
.welcome .btn{position:absolute;left:327px;top:98px;width:55px;height:20px;background:var(--teal)}

/* pricing */
.section-title{font-family:"Montserrat",sans-serif;font-weight:700;font-size:14px;color:var(--grey-title);text-transform:uppercase}
.pricing-title{left:0;top:526px;width:709px;text-align:center}
.plan{top:570px;width:109px;height:133px;border:1px solid var(--line);background:var(--white)}
.plan-head{height:28px;display:flex;align-items:center;justify-content:space-between;padding:0 8px 0 9px;color:var(--white);margin:-1px -1px 0}
.plan-name{font-family:"Montserrat",sans-serif;font-weight:700;font-size:8px;text-transform:uppercase}
.plan-price{font-family:"Montserrat",sans-serif;font-weight:700;font-size:14px}
.plan-price small{font-size:8px}
.plan ul{list-style:none;margin:4px 9px 0}
.plan li{font-style:italic;font-size:6.5px;color:var(--muted);text-align:center;height:20px;line-height:20px;border-bottom:1px solid var(--line)}
.plan li:nth-child(3){height:23px;line-height:23px}
.plan .btn{position:absolute;left:28px;top:108px;width:50px;height:18px;border-radius:5px}
.silver{left:174px}.silver .plan-head,.silver .btn{background:var(--teal)}
.gold{left:300px}.gold .plan-head,.gold .btn{background:var(--gold)}
.platinum{left:426px}.platinum .plan-head,.platinum .btn{background:var(--red)}

/* demo */
.demo-title{left:118px;top:768px}
.demo-text{left:118px;top:790px;width:190px;font-size:6.5px;line-height:16px;color:var(--text)}
.field{border:1px solid #c9c9c9;border-radius:5px;font-size:5.5px;color:#666;padding:5px 8px;text-transform:uppercase;background:var(--white)}
.f-name{left:118px;top:830px;width:80px;height:18px}
.f-phone{left:202px;top:830px;width:80px;height:18px}
.f-email{left:118px;top:853px;width:165px;height:17px}
.f-msg{left:118px;top:875px;width:165px;height:31px}
.submit{left:119px;top:910px;width:50px;height:18px;background:var(--navy)}
.video{left:335px;top:772px;width:249px;height:155px;background:linear-gradient(100deg,#2a2420 0%,#5a4838 40%,#3b2f27 70%,#1e1a17 100%);box-shadow:0 8px 8px -6px rgba(0,0,0,.35)}

/* footer */
.site-footer{left:0;top:957px;width:709px;height:185px;background:var(--footer-bg)}
.footer-brand{left:124px;top:980px}
.about-title{left:124px;top:1003px;font-size:11px;color:#555}
.about-text{left:124px;top:1022px;width:179px;font-size:6px;line-height:16px;text-align:justify;color:var(--text)}
.about-btn{left:123px;top:1109px;width:63px;height:18px;background:var(--navy)}
.contact-title{left:372px;top:1003px;font-size:11px;color:#555}
.contact-info{left:374px;top:1025px;font-size:6px;line-height:15.5px;color:var(--text)}
.contact-info .gap{height:8px}
.map{left:460px;top:1017px;width:123px;height:89px;background:linear-gradient(135deg,#cfe0c4 0%,#e8e4d6 45%,#8fc1e6 70%,#d9e4cc 100%)}

.bottom-bar{left:0;top:1142px;width:709px;height:34px;background:var(--white);box-shadow:0 -1px 3px rgba(0,0,0,.08)}
.social{top:1151px;width:21px;height:20px;border:1px solid #ddd;background:var(--white)}
.social.filled{background:var(--navy);border-color:var(--navy)}
.social span{position:absolute;left:7px;top:7px;width:5px;height:5px;background:#999}
.social.filled span{background:var(--white)}
.footer-nav{right:122px;top:1152px;display:flex;gap:15px;font-family:"Montserrat",sans-serif;font-size:7.5px;color:#555}
.copyright{right:123px;top:1183px;font-size:6.5px;color:#333}
</style>
</head>
<body>

<header class="site-header abs">
  <div class="brand abs"><span class="brand-mark"></span>Velora Nexa</div>
  <nav class="main-nav abs">
    <span class="active">Home</span><span>Intro</span><span>Pricing</span><span>Demo</span><span>About Us</span><span>Contact</span>
  </nav>
</header>

<section class="hero abs" role="img" aria-label="Two garden centre staff in a greenhouse, one holding a potted flowering plant, the other a tablet">
  <svg class="play abs" width="14" height="18" viewBox="0 0 14 18"><path d="M0 0 L14 9 L0 18 Z" fill="#fff"/></svg>
</section>

<section class="welcome abs">
  <h1>WELCOME TO VELORA NEXA</h1>
  <p>Nor again is there anyone who loves or pursues or desires to obtain pain of itself, because it is pain, but because occasionally circumstances occur in which toil and pain can procure him some great pleasure. To take a trivial example, which of us ever undertakes laborious physical exercise,</p>
  <a class="btn">Read More</a>
</section>

<h2 class="section-title pricing-title abs">Pricing</h2>

<div class="plan silver abs">
  <div class="plan-head"><span class="plan-name">Silver</span><span class="plan-price">19/<small>$</small></span></div>
  <ul><li>Lorium ipsum</li><li>Sed Amit Dolor</li><li>Dolor Duis eno</li></ul>
  <a class="btn">Sign Up</a>
</div>
<div class="plan gold abs">
  <div class="plan-head"><span class="plan-name">Gold</span><span class="plan-price">199/<small>$</small></span></div>
  <ul><li>Lorium ipsum</li><li>Sed Amit Dolor</li><li>Dolor Duis eno</li></ul>
  <a class="btn">Sign Up</a>
</div>
<div class="plan platinum abs">
  <div class="plan-head"><span class="plan-name">Platinum</span><span class="plan-price">299/<small>$</small></span></div>
  <ul><li>Lorium ipsum</li><li>Sed Amit Dolor</li><li>Dolor Duis eno</li></ul>
  <a class="btn">Sign Up</a>
</div>

<h2 class="section-title demo-title abs">Schedule a Demo</h2>
<p class="demo-text abs">Sed ut perspiciatis unde omnis iste natus error sit voluptatem accusantium doloremque....</p>
<div class="field f-name abs">Name</div>
<div class="field f-phone abs">Phone</div>
<div class="field f-email abs">Email</div>
<div class="field f-msg abs">Message</div>
<a class="btn submit abs">Submit</a>
<div class="video abs" role="img" aria-label="Product tour video: a woman using a tablet at a café table">
  <svg class="play abs" width="48" height="48" viewBox="0 0 48 48"><circle cx="24" cy="24" r="22" fill="none" stroke="rgba(255,255,255,.6)" stroke-width="2.5"/><path d="M19 14 L33 24 L19 34 Z" fill="#fff"/></svg>
</div>

<footer class="site-footer abs"></footer>
<div class="brand footer-brand abs"><span class="brand-mark"></span>Velora Nexa</div>
<h3 class="section-title about-title abs">About Us</h3>
<p class="about-text abs">Velora Nexa platform is digitizing Brick &amp; Mortar chains by offering complete sourcing to sales integration allowing realtime visibility and control over every aspect of its business. Chains can immediately become omni channel increasing their reach and providing innovative customer experiences.</p>
<a class="btn about-btn abs">Read More</a>

<h3 class="section-title contact-title abs">Contact Us</h3>
<div class="contact-info abs">
  <div>Phone : 1-800 555 0142</div>
  <div>Email : hello@veloranexa.co</div>
  <div class="gap"></div>
  <div>Address : Velora Nexa</div>
  <div>Level 12, 48 Harbour Lane</div>
  <div>Eastport NSW 2100</div>
</div>
<div class="map abs" role="img" aria-label="Street map showing the office location by the harbour"></div>

<div class="bottom-bar abs"></div>
<div class="social filled abs" style="left:122px"><span></span></div>
<div class="social abs" style="left:149px"><span></span></div>
<div class="social abs" style="left:176px"><span></span></div>
<div class="social abs" style="left:203px"><span></span></div>
<nav class="footer-nav abs"><span>Home</span><span>Intro</span><span>Pricing</span><span>Demo</span><span>About Us</span><span>Contact</span></nav>
<p class="copyright abs">© 2016. www.veloranexa.co</p>

</body>
</html>
```